Bright Current Electrical & Communications business card design

We would like a double sided business card that is different. Want it to be exciting and fun. Something that people keep rather then just throw it in the bin.
We have a logo that we want to put on one side of the business card and then the business information on the reverse side. Trying to go for a real professional style of business card

Target Market(s)

Electrical

Industry/Entity Type

Electrical

Contact Information for Business Card

Bright Current Electrical & Communications
Darren Kellaway
P: 0437 862 305
E: brightcurrent@mailbox-example.com.au
Lic No: 574106K
24/7

Font styles to use
Other font styles liked:
• Would like ideas

Requirements
Must have
• Our company logo (preferably on both sides) yellow needs to be incorporated somewhere. Business card card colours to match with logo. Maybe a small pop of colour
Nice to have
• Open to some design ideas

```html
<!DOCTYPE html>
<html lang="en">
<head>
<meta charset="utf-8">
<title>Bright Current Electrical &amp; Communications – Business Card</title>
<link href="https://fonts.googleapis.com/css2?family=Montserrat:wght@500;600;800&family=Audiowide&family=Open+Sans:wght@600&display=swap" rel="stylesheet">
<style>
  :root {
    --backdrop: #5e5e5e;
    --card-yellow: #e9ee72;
    --card-grey: #8e8e8a;
    --logo-grey: #5f5a5b;
    --ink: #161616;
    --accent-yellow: #f2f21c;
    --alert-red: #e3141b;
    --name-green: #4f6b1f;
    --bar-grey: #9a9a9a;
    --bar-text: #ffffff;
  }
  * { box-sizing: border-box; margin: 0; padding: 0; }
  html, body { width: 1200px; height: 1000px; overflow: hidden; }
  body {
    background: var(--backdrop);
    position: relative;
    font-family: "Montserrat", Arial, sans-serif;
    color: var(--ink);
  }
  .card {
    position: absolute;
    top: 360px;
    width: 486px;
    height: 306px;
    background: linear-gradient(115deg, var(--card-yellow) 0%, #d0d47a 40%, var(--card-grey) 100%);
    box-shadow: 0 4px 14px rgba(0,0,0,0.45);
    overflow: hidden;
  }
  .card--front { left: 94px; }
  .card--back { left: 625px; }

  .brand-mark {
    position: absolute;
    left: 0; right: 0;
    text-align: center;
    font-family: "Montserrat", Arial, sans-serif;
    font-weight: 800;
    color: var(--logo-grey);
    letter-spacing: 6px;
    line-height: 1;
  }
  .card--front .brand-mark { top: 78px; font-size: 92px; }
  .card--back .brand-mark { top: 36px; font-size: 58px; left: 12px; letter-spacing: 4px; }

  .company-name {
    position: absolute;
    left: 0; right: 0;
    text-align: center;
    font-weight: 600;
    letter-spacing: 1.5px;
    white-space: nowrap;
  }
  .card--front .company-name { top: 186px; font-size: 21px; }
  .card--back .company-name { top: 106px; font-size: 14px; left: 12px; }

  .company-tagline {
    position: absolute;
    left: 0; right: 0;
    display: flex;
    align-items: center;
    justify-content: center;
    gap: 8px;
    font-weight: 500;
    letter-spacing: 1px;
  }
  .company-tagline::before,
  .company-tagline::after {
    content: "";
    height: 1.5px;
    background: var(--accent-yellow);
  }
  .card--front .company-tagline { top: 217px; font-size: 14px; }
  .card--front .company-tagline::before,
  .card--front .company-tagline::after { width: 80px; }
  .card--back .company-tagline { top: 127px; font-size: 9px; left: 12px; }
  .card--back .company-tagline::before,
  .card--back .company-tagline::after { width: 55px; }

  .corner-flag { position: absolute; left: 0; top: 0; }

  .holder-name {
    position: absolute;
    left: 97px; top: 143px;
    width: 303px; height: 29px;
    background: linear-gradient(90deg, var(--name-green) 0%, #6b7a3c 80%, #8a8d7a 100%);
    box-shadow: 2px 2px 4px rgba(0,0,0,0.35);
    font-family: "Audiowide", sans-serif;
    font-size: 20px;
    color: transparent;
    -webkit-text-stroke: 1px var(--accent-yellow);
    text-align: center;
    line-height: 29px;
    letter-spacing: 1px;
    white-space: nowrap;
  }
  .licence {
    position: absolute;
    left: 176px; top: 178px;
    font-family: "Open Sans", Arial, sans-serif;
    font-size: 15px;
  }
  .contact-bar {
    position: absolute;
    height: 22px;
    background: var(--bar-grey);
    box-shadow: 3px 3px 5px rgba(0,0,0,0.4);
    color: var(--bar-text);
    font-family: "Open Sans", Arial, sans-serif;
    font-weight: 600;
    line-height: 22px;
    white-space: nowrap;
  }
  .contact-bar--phone { left: 0; top: 210px; width: 168px; font-size: 15px; padding-left: 24px; }
  .contact-bar--email { right: 0; top: 236px; width: 300px; font-size: 12.5px; padding-left: 8px; }
</style>
</head>
<body>
  <section class="card card--front" aria-label="Business card front">
    <div class="brand-mark">BCEC</div>
    <div class="company-name">BRIGHT CURRENT ELECTRICAL</div>
    <div class="company-tagline">&amp; COMMUNICATIONS</div>
  </section>

  <section class="card card--back" aria-label="Business card back">
    <svg class="corner-flag" width="120" height="90" viewBox="0 0 120 90" aria-label="24 hour service">
      <line x1="0" y1="88" x2="112" y2="0" stroke="var(--alert-red)" stroke-width="2"/>
      <text x="30" y="60" transform="rotate(-38 30 60)" font-family="Montserrat, Arial, sans-serif" font-weight="800" font-size="17" fill="var(--alert-red)">24H</text>
    </svg>
    <div class="brand-mark">BCEC</div>
    <div class="company-name">BRIGHT CURRENT ELECTRICAL</div>
    <div class="company-tagline">&amp; COMMUNICATIONS</div>
    <div class="holder-name">DARREN KELLAWAY</div>
    <div class="licence">Lic No: 574106K</div>
    <div class="contact-bar contact-bar--phone">0437 862 305</div>
    <div class="contact-bar contact-bar--email">brightcurrent@mailbox-example.com.au</div>
  </section>
</body>
</html>
```